Interpretive Signs x 2

We would like 2 x Aboriginal themed signs. Design to be relaxed, contemporary, clean, fresh, inspiring natural Aboriginal themes tying in traditional elements.

Sign 1: Meeting Place - A1 sized (or A0 if better for design/layout)
Sign 2: The Six Seasons - A2 (or A1 if better for design/layout)
See file 12 for proposed layout (this is just an idea I had - it doesn't have to be like this!)

Requirements
Must have
• Use the symbols provided. Primarily use images provided. See our website www.tallowbrookfarm.com.au for our branding style. Stock images for fire etc ok as long as they do not show a location. If using any stock images of trees etc, they must be native to South West WA (ie Karri, Jarrah, Marri).
Nice to have
• Fonts preferred to be "Softer than Rain" as attached if this works with design - but not essential.

Perhaps use our logo colors where possible/appropriate - not essential!
Should not have
• Anything that breaches Aboriginal copyright or IP. The design elements must be generic with an Aboriginal theme and not be specifically representative of other Aboriginal people from other regions.

Any depictions of nature or Aboriginal people must be relevant to the South West of Western Australia - and not show nature or culture which does not belong here.

No pictures of trees or landscapes (mountains etc) which are clearly not from here (we have no mountains - just forest).

```html
<!DOCTYPE html>
<html lang="en">
<head>
<meta charset="utf-8">
<title>Kayabora – Meeting Place Sign</title>
<link rel="stylesheet" href="https://fonts.googleapis.com/css2?family=Amatic+SC:wght@700&family=Open+Sans:wght@400;600&display=swap">
<style>
  :root{
    --green-dark:#2e7433;
    --green:#3f8e3c;
    --green-light:#8cc43f;
    --leaf-pale:#e4efd6;
    --text:#3b3b3b;
    --paper:#ffffff;
  }
  *{box-sizing:border-box;margin:0;padding:0}
  html,body{width:859px;height:1200px;overflow:hidden;background:var(--paper)}
  .sign{position:relative;width:859px;height:1200px;background:var(--paper);font-family:"Open Sans",Arial,sans-serif;color:var(--text)}
  .brand{position:absolute;left:24px;top:22px;display:flex;align-items:center;gap:10px}
  .brand-dot{width:44px;height:44px;border-radius:50%;background:var(--green)}
  .brand-name{font-weight:600;font-size:15px;color:var(--green);letter-spacing:1px;text-transform:uppercase;line-height:1.15}
  .brand-tag{position:absolute;left:78px;top:68px;font-size:8px;color:var(--green);letter-spacing:2px;text-transform:uppercase;font-weight:600}
  .title{position:absolute;left:0;right:0;top:12px;text-align:center;font-family:"Amatic SC",cursive;font-weight:700;font-size:96px;letter-spacing:10px;color:var(--green)}
  .header-tree{position:absolute;right:10px;top:6px;width:130px;height:112px;border-radius:50% 50% 40% 40%;background:radial-gradient(circle at 50% 40%,#b7d98a,#6fae3f)}
  .section{position:absolute;left:0;width:859px}
  .symbol{position:absolute;left:30px;top:8px;width:110px;height:110px;border-radius:10px;background:var(--leaf-pale)}
  .band{position:absolute;left:168px;right:0;top:0;height:30px;background:linear-gradient(90deg,var(--green-dark),var(--green-light));color:#fff;font-family:"Amatic SC",cursive;font-weight:700;font-size:25px;letter-spacing:1.5px;line-height:31px;padding-left:14px;text-transform:uppercase;white-space:nowrap;overflow:hidden}
  .body{position:absolute;left:182px;right:26px;top:40px;font-size:9.5px;line-height:1.45}
  .body p{margin-bottom:4px}
  .s1{top:140px}.s2{top:372px}.s3{top:540px}.s4{top:748px}
  .photos{position:absolute;left:20px;right:20px;top:905px;height:212px;display:flex;gap:10px}
  .photo{flex:1;border-radius:2px}
  .photo-leaves{background:linear-gradient(160deg,#4f7d2e,#1f3b18)}
  .photo-bush{background:linear-gradient(180deg,#9bb87a,#3d5a2c)}
  .photo-fire{background:radial-gradient(circle at 50% 70%,#f6a323,#b34a12 40%,#2a1a10 80%)}
  .footer{position:absolute;left:0;right:0;top:1130px;height:50px;background:linear-gradient(90deg,var(--green-dark),var(--green-light));color:#fff;font-size:10px;line-height:16px;padding:9px 26px;text-align:center}
</style>
</head>
<body>
<main class="sign">
  <header>
    <div class="brand"><span class="brand-dot"></span><span class="brand-name">Tallowbrook<br>Farm</span></div>
    <div class="brand-tag">Bush Retreat</div>
    <h1 class="title">KAYABORA</h1>
    <div class="header-tree" role="img" aria-label="Illustration of a native South West marri tree"></div>
  </header>

  <section class="section s1">
    <div class="symbol" role="img" aria-label="Aboriginal meeting place symbol"></div>
    <h2 class="band">Bora – The Meeting Place</h2>
    <div class="body">
      <p>This “Meeting Place” is for guests of Tallowbrook Farm to enjoy spending time together. It enables people to connect with the local landscape and traditional culture.</p>
      <p>Cultural and environmental presentations, performances, social gatherings and group meetings can be held in this natural bush amphitheatre.</p>
      <p>It is also a place for people to relax and enjoy being amidst nature. During winter, groups may choose to light a fire in the designated fire pit within the centre, so that you can share stories and keep warm.</p>
      <p>Please respect the “Meeting Place”. Ensure children are well supervised and litter is not thrown into the fire or left in this special place.</p>
      <p>This is a place to reflect on nature and culture.</p>
    </div>
  </section>

  <section class="section s2">
    <div class="symbol" role="img" aria-label="Aboriginal coming together symbol"></div>
    <h2 class="band">Bidi – Meeting or coming together. A traditional perspective</h2>
    <div class="body">
      <p>Traditionally local Aboriginal people moved through Country for hunting and gathering, though often came together for meetings and ceremonies. They moved within their traditional boundaries which for the Wardandi people is framed by the Preston River, following along the escarpment, and down to the Blackwood River in the south.</p>
      <p>Wardandi people camped in this area. Extensive shelters built out of natural bush materials near their meeting place. The meeting trees and places were chosen by the seasons and were for trading news, medicine, information and knowledge.</p>
    </div>
  </section>

  <section class="section s3">
    <div class="symbol" role="img" aria-label="Aboriginal people symbol"></div>
    <h2 class="band">The local Aboriginal people – The Wardandi</h2>
    <div class="body">
      <p>The Wardandi (Saltwater) people lived by the sea and are one of the Noongar tribes, and are the Traditional Owners of the South West Cape to Cape region. The region’s wide variety of natural foods, wonderful beaches, forests and river systems are traditional pathways to the meeting of the Wardandi’s cultural custodians.</p>
      <p>“Caring for country” is integral to culture, land and future, and by respecting Country visitors show their respect and contribute to our environmental sustainability.</p>
      <p>Living by the six seasons, the Wardandi people hunted and gathered from the land and sea. They would move along the coastal areas during the warmer months, and then back along the wetlands, river systems and lakes over the cooler months. They would hunt for traditional foods such as kangaroo, wallaby, emu, ducks, birds, fish, squid, octopus, crab, marron, abalone, and a large variety of bush vegetables and fruits.</p>
    </div>
  </section>

  <section class="section s4">
    <div class="symbol" role="img" aria-label="Aboriginal fire symbol"></div>
    <h2 class="band">The significance of Kaala (fire) to the Wardandi people</h2>
    <div class="body">
      <p>Fire is an important part of Aboriginal culture, of expressions family and society. Traditionally fire is used for cooking food, warmth, hunting, ceremonies and caring for country, cleansing the spirits, burials and land management.</p>
      <p>Aboriginal people carefully set fire to the bush in autumn, using mosaic (cool) burning, to make way for regeneration and allow the new plant growth to attract animals for hunting. Controlled, low heat burns aim to help restore the traditional knowledge that if the soil litter and combustion are kept lower, destructive bushfires can be avoided.</p>
      <p>Traditional fire making by using our materials found in the natural environment is a skill that takes a lot of practice, and is done using a fire drill and a fire saw.</p>
    </div>
  </section>

  <div class="photos">
    <div class="photo photo-leaves" role="img" aria-label="Photo of native marri leaves and gum nuts"></div>
    <div class="photo photo-bush" role="img" aria-label="Photo of native bush plants in the forest"></div>
    <div class="photo photo-fire" role="img" aria-label="Photo of a campfire burning in the fire pit"></div>
  </div>

  <footer class="footer">
    PO Box 00 Ferndale WA 6000 · Tallowbrook Farm, 12 Example Road, Ferndale WA 6000<br>
    www.tallowbrookfarm.com.au · E stay@tallowbrookfarm.com.au · T 08 5550 1234 · M 0400 555 000
  </footer>
</main>
</body>
</html>
```